High Tech Real Estate Startup needs a business card

We are developing an innovative real estate marketing product based around advanced search and virtual reality.

We talk to people, we need business cards.

Target Market(s)

The target market is technology professionals and realtors.

Contact Information for Business Card

The information to be included will include

Name
Title
Phone Number
E-mail Address
www.quelzo.com

It should use simple iconography for each one of those fields.

Font styles to use
Other font styles liked:
• Co, Jubilat, Avenir

Colors

Designer to choose colors to be used in the design.

Requirements
Must have
• Clean aesthetic,
• Good use of negative space.
• It should use our company logo, shown in the attached file. It is able to use the negative of that logo (coloured font and white background) and I have attached other acceptable accent colours in a swatch file.
Should not have
• Should not be too busy
• No extraneous text (slogans, tag lines etc)

```html
<!DOCTYPE html>
<html lang="en">
<head>
<meta charset="utf-8">
<title>Quelzo Business Card</title>
<link rel="stylesheet" href="https://fonts.googleapis.com/css2?family=Lato:wght@400;700&display=swap">
<style>
  :root {
    --stage: #3d3d3d;
    --paper: #ffffff;
    --teal: #00b5bd;
    --teal-light: #33c4ca;
    --teal-deep: #009aa1;
    --ink: #1a1a1a;
    --rule: #8c8cb4;
  }
  * { margin: 0; padding: 0; box-sizing: border-box; }
  html, body {
    width: 1200px;
    height: 900px;
    overflow: hidden;
    background: var(--stage);
    font-family: "Lato", sans-serif;
  }
  .stage { position: relative; width: 1200px; height: 900px; }

  .card {
    position: absolute;
    top: 170px;
    width: 347px;
    height: 561px;
  }
  .card--front { left: 259px; background: var(--paper); }
  .card--back { left: 631px; overflow: hidden; }

  .wordmark {
    position: absolute;
    left: 0;
    width: 100%;
    text-align: center;
    font-weight: 700;
    letter-spacing: 2px;
    line-height: 1;
  }
  .card--front .wordmark { top: 172px; font-size: 64px; color: var(--teal); }
  .card--back .wordmark { top: 250px; font-size: 66px; color: var(--paper); }

  .pattern-field {
    position: absolute;
    inset: 0;
    background: linear-gradient(160deg, var(--teal-light) 0%, var(--teal) 45%, var(--teal-deep) 100%);
  }

  .contact {
    position: absolute;
    left: 0;
    top: 386px;
    width: 100%;
    text-align: center;
    color: var(--ink);
  }
  .contact__name {
    font-size: 21px;
    font-weight: 700;
    color: var(--teal);
    letter-spacing: 0.5px;
    line-height: 1;
  }
  .contact__title { font-size: 14.5px; margin-top: 6px; line-height: 1.2; }
  .contact__rule {
    width: 156px;
    height: 1px;
    background: var(--rule);
    margin: 10px auto 12px;
  }
  .contact__line { font-size: 14.5px; line-height: 21px; }
  .contact__label { color: var(--teal); font-weight: 700; }
  .contact__web { font-size: 14.5px; line-height: 22px; color: var(--teal); font-weight: 700; }
</style>
</head>
<body>
<main class="stage">
  <section class="card card--front">
    <div class="wordmark">QUELZO</div>
    <div class="contact">
      <p class="contact__name">DANA WRIGHT</p>
      <p class="contact__title">Managing Director</p>
      <div class="contact__rule"></div>
      <p class="contact__line"><span class="contact__label">P:</span> 555-014-2379</p>
      <p class="contact__line"><span class="contact__label">E:</span> hello@quelzo.com</p>
      <p class="contact__web">www.quelzo.com</p>
    </div>
  </section>

  <section class="card card--back">
    <div class="pattern-field" role="img" aria-label="Diagonal repeating brand-name pattern in tonal teal"></div>
    <div class="wordmark">QUELZO</div>
  </section>
</main>
</body>
</html>
```